Design Business Card MAPLE WREN MOWING

We have attached a copy of our Logo, we like a business card designed with logo and mobile phone number on one side that stands out maybe gloss and on the other side it can have the services we do small picture of our logo name number, I have attached an idea to this that I have seen online, this is a business owned by a woman so we like pinks black and navy
Our logo is attached in pdf
Target Market(s)
Home owners that need lawns mowed
Industry/Entity Type
Lawns and gardens
Contact Information for Business Card
Logo business Owner name Deborah Finch mobile number 0491627504
Font styles to use
Look and feel
Each slider illustrates characteristics of the customer's brand and the style your logo design should communicate.

```html
<!DOCTYPE html>
<html lang="en">
<head>
<meta charset="utf-8">
<title>Maple Wren Mowing – Business Card</title>
<link rel="stylesheet" href="https://fonts.googleapis.com/css2?family=Montserrat:wght@400;500;800&family=Oswald:wght@600&display=swap">
<style>
  :root {
    --stage: #3a3a3c;
    --pink: #de3a93;
    --pink-deep: #d02c86;
    --pink-light: #e85aa6;
    --green: #3fb54a;
    --white: #ffffff;
    --ink: #1b1b1b;
  }
  * { box-sizing: border-box; margin: 0; padding: 0; }
  html, body { width: 1200px; height: 1200px; overflow: hidden; }
  body {
    background: var(--stage);
    display: flex;
    flex-direction: column;
    align-items: center;
    justify-content: center;
    gap: 56px;
    font-family: "Montserrat", sans-serif;
  }
  .card {
    position: relative;
    width: 900px;
    height: 514px;
    border-radius: 34px;
    overflow: hidden;
  }

  /* ---------- Info side ---------- */
  .card-info { background: var(--white); }
  .info-top {
    position: absolute; left: 0; right: 0; top: 0; height: 262px;
    display: flex; align-items: center; justify-content: center;
    padding-right: 80px;
  }
  .stripe {
    position: absolute; left: 0; right: 0; top: 262px; height: 14px;
    background: var(--green);
  }
  .info-bottom {
    position: absolute; left: 0; right: 0; top: 276px; bottom: 0;
    background: linear-gradient(100deg, var(--pink-deep), var(--pink) 55%, var(--pink-light));
  }
  .contact {
    position: absolute; left: 84px; bottom: 62px; color: var(--white);
  }
  .contact-name { font-size: 34px; font-weight: 500; letter-spacing: 1px; line-height: 1; }
  .contact-role { font-size: 18px; font-weight: 400; letter-spacing: 1px; margin: 4px 0 0 24px; }
  .contact-phone {
    display: flex; align-items: center; gap: 14px;
    margin: 16px 0 0 48px; font-size: 38px; font-weight: 800; letter-spacing: 1px;
  }
  .contact-phone svg { width: 38px; height: 38px; }
  .divider {
    position: absolute; left: 520px; top: 300px; width: 1px; height: 150px;
    background: rgba(255,255,255,.55);
  }
  .services {
    position: absolute; left: 590px; top: 292px;
    list-style: none; color: var(--white);
    font-family: "Oswald", sans-serif; font-weight: 600;
    font-size: 24px; letter-spacing: 1px; line-height: 1.15;
  }
  .services li { display: flex; align-items: center; gap: 10px; }
  .services li::before {
    content: ""; width: 8px; height: 8px; border-radius: 50%; background: var(--green);
  }

  /* ---------- Brand mark (text lockup) ---------- */
  .brand { display: flex; align-items: center; gap: 16px; }
  .brand-dot { border-radius: 50%; flex: none; }
  .brand-name { font-weight: 800; letter-spacing: 1px; white-space: nowrap; }
  .brand-small .brand-dot { width: 54px; height: 54px; background: var(--pink); }
  .brand-small .brand-name { font-size: 34px; color: var(--ink); }

  /* ---------- Logo side ---------- */
  .card-logo {
    background: linear-gradient(100deg, var(--pink-deep), var(--pink) 50%, var(--pink-light));
    display: flex; align-items: center; justify-content: center;
  }
  .brand-large .brand-dot { width: 110px; height: 110px; background: var(--ink); }
  .brand-large .brand-name { font-size: 58px; color: var(--white); }
</style>
</head>
<body>

  <section class="card card-info" aria-label="Business card, contact side">
    <div class="info-top">
      <div class="brand brand-small">
        <span class="brand-dot"></span>
        <span class="brand-name">MAPLE WREN MOWING</span>
      </div>
    </div>
    <div class="stripe"></div>
    <div class="info-bottom">
      <div class="contact">
        <p class="contact-name">DEBORAH FINCH</p>
        <p class="contact-role">OWNER</p>
        <p class="contact-phone">
          <svg viewBox="0 0 40 40" aria-hidden="true">
            <circle cx="20" cy="20" r="20" fill="#fff"/>
            <path d="M14 10c1-1 2.5-1 3 .3l1.6 3.6c.4 1 0 1.8-.7 2.4l-1.2 1c1 2.4 3 4.5 5.4 5.6l1-1.2c.6-.7 1.5-1 2.4-.6l3.6 1.6c1.2.5 1.3 2 .3 3l-1.8 1.8c-1 1-2.6 1.2-4 .6C19 26.6 14 21.6 12.5 15.4c-.4-1.4 0-3 1-4z" fill="#de3a93"/>
          </svg>
          049.162.7504
        </p>
      </div>
    </div>
    <div class="divider"></div>
    <ul class="services">
      <li>GARDEN MAINTENANCE</li>
      <li>RUBBISH REMOVAL</li>
      <li>TRIMMING</li>
      <li>WEEDING</li>
      <li>LAWN CARE</li>
    </ul>
  </section>

  <section class="card card-logo" aria-label="Business card, logo side">
    <div class="brand brand-large">
      <span class="brand-dot"></span>
      <span class="brand-name">MAPLE WREN MOWING</span>
    </div>
  </section>

</body>
</html>
```